Brantley Advisory Group provides support for renewable energy projects to utilities and suppliers

I need a professional looking business card that is both simple and elegant and unique. My clients are mostly large organizations not individuals. I am a consultant with my own company that is small but would like to give clients the impression I am larger. Smart grid, fiber optics, software, field hardware, distribution automation, substation automation, operations, energy storage/batteries, microgrids, customer service, strategy/roadmaps, conservation, Automated Metering Infrastruture (AMI or smart meters) are all areas of focus.

Target Market(s)

Utilities, suppliers, governmental agencies involved in energy. All types of energy especially natural gas and electrical. Especially renewable energy or green projects.

Contact Information for Business Card

Name - Mark Brantley Cell Phone - 425.318.2746 Email - mbrantley@brantleyag-example.com
Company - Brantley Advisory Group (logo) Title - Principal

Font styles to use
Serif
Sans Serif

Colors

Designer to choose colors to be used in the design.

Requirements
Must have
• Simple and professional and powerful.
• Unique/creative design.
Nice to have
• Utilize color scheme to accent logo colors. Maybe some geometric pattern on edge of card with color.
Should not have
• Busy, complicated, traditional

```html
<!DOCTYPE html>
<html lang="en">
<head>
<meta charset="utf-8">
<title>Brantley Advisory Group – Business Card</title>
<link rel="stylesheet" href="https://fonts.googleapis.com/css2?family=Montserrat:wght@400;600;700&display=swap">
<style>
  :root {
    --backdrop: #a4a4a4;
    --brand-blue: #1a1fa8;
    --brand-blue-deep: #0d12a0;
    --brand-blue-light: #2f36c2;
    --brand-green: #5b9a3a;
    --paper: #ffffff;
    --ink: #3a3a3a;
  }
  html, body {
    margin: 0;
    padding: 0;
    width: 1200px;
    height: 982px;
    overflow: hidden;
    background: var(--backdrop);
    font-family: "Montserrat", sans-serif;
  }
  .stage {
    position: relative;
    width: 1200px;
    height: 982px;
  }
  .card {
    position: absolute;
    top: 228px;
    width: 300px;
    height: 525px;
    overflow: hidden;
    box-shadow: 0 10px 24px rgba(0,0,0,0.25);
  }
  .card-front { left: 250px; background: var(--paper); }
  .card-back {
    left: 650px;
    background: radial-gradient(ellipse at 55% 38%, var(--brand-blue-light) 0%, var(--brand-blue) 45%, var(--brand-blue-deep) 100%);
  }

  .brand {
    position: absolute;
    display: flex;
    align-items: center;
    gap: 10px;
  }
  .brand-mark {
    width: 22px;
    height: 22px;
    border: 3px solid currentColor;
    border-radius: 3px;
    flex: none;
  }
  .brand-name {
    font-weight: 700;
    font-size: 20px;
    line-height: 1.15;
    letter-spacing: 0.5px;
  }
  .card-front .brand { top: 62px; left: 40px; color: var(--brand-blue); }
  .card-back .brand { top: 170px; left: 38px; color: #fff; }
  .card-back .brand-name { font-size: 22px; }

  .name-band {
    position: absolute;
    left: 0;
    top: 205px;
    width: 100%;
    height: 82px;
    background: var(--brand-blue);
    color: #fff;
    box-sizing: border-box;
    padding: 20px 0 0 60px;
  }
  .person-name {
    margin: 0;
    font-weight: 700;
    font-size: 24px;
    letter-spacing: 1.5px;
  }
  .person-title {
    margin: 2px 0 0;
    font-weight: 400;
    font-size: 13px;
    letter-spacing: 0.5px;
  }

  .contact-list {
    position: absolute;
    left: 60px;
    top: 378px;
    margin: 0;
    padding: 0;
    list-style: none;
    color: var(--ink);
    font-size: 11.5px;
  }
  .contact-list li {
    display: flex;
    align-items: center;
    gap: 8px;
    height: 19px;
  }
  .contact-icon { width: 13px; height: 13px; flex: none; }

  .bottom-wave {
    position: absolute;
    left: 0;
    bottom: 0;
    width: 300px;
    height: 110px;
  }
</style>
</head>
<body>
<main class="stage">

  <section class="card card-front">
    <div class="brand">
      <span class="brand-mark"></span>
      <span class="brand-name">Brantley<br>Advisory Group</span>
    </div>

    <div class="name-band">
      <h1 class="person-name">Mark Brantley</h1>
      <p class="person-title">Principal</p>
    </div>

    <ul class="contact-list">
      <li>
        <svg class="contact-icon" viewBox="0 0 14 14" fill="none" stroke="var(--brand-blue)" stroke-width="1.1">
          <rect x="0.6" y="0.6" width="12.8" height="12.8" rx="2.5"/>
          <path d="M4 3.5c0 3.5 2.5 6.5 6 7l0.8-1.6-1.8-1-0.9 0.8c-1-0.5-1.8-1.4-2.3-2.4l0.8-0.8-1-1.8z" fill="var(--brand-blue)" stroke="none"/>
        </svg>
        <span>425.318.2746</span>
      </li>
      <li>
        <svg class="contact-icon" viewBox="0 0 14 14" fill="none" stroke="var(--brand-blue)" stroke-width="1.1">
          <rect x="0.6" y="0.6" width="12.8" height="12.8" rx="2.5"/>
          <rect x="3" y="4.3" width="8" height="5.6"/>
          <path d="M3 4.5l4 3 4-3"/>
        </svg>
        <span>mbrantley@brantleyag-example.com</span>
      </li>
      <li>
        <svg class="contact-icon" viewBox="0 0 14 14" fill="none" stroke="var(--brand-blue)" stroke-width="1.1">
          <rect x="0.6" y="0.6" width="12.8" height="12.8" rx="2.5"/>
          <circle cx="7" cy="7" r="3.8"/>
          <path d="M3.2 7h7.6M7 3.2c-1.8 2.2-1.8 5.4 0 7.6M7 3.2c1.8 2.2 1.8 5.4 0 7.6"/>
        </svg>
        <span>www.brantleyag-example.com</span>
      </li>
    </ul>

    <svg class="bottom-wave" viewBox="0 0 300 110" preserveAspectRatio="none" aria-hidden="true">
      <path d="M0 78 C120 92 230 70 300 8 L300 110 L0 110 Z" fill="var(--brand-blue)"/>
      <path d="M70 80 C160 82 240 60 300 2" fill="none" stroke="var(--brand-green)" stroke-width="2.5"/>
    </svg>
  </section>

  <section class="card card-back">
    <div class="brand">
      <span class="brand-mark"></span>
      <span class="brand-name">Brantley<br>Advisory Group</span>
    </div>
  </section>

</main>
</body>
</html>
```